Trade Show Booth Design for Candy Specialty and gift trade show

Thornwell Brands is known across America and carries a long heritage of award-winning confectionery products, quality, and staying power: Keswick & Yardley® Rock Candy was introduced in 1880, Thornwell Mints in 1893, and Pelmarr® Candy Sticks in 1945. The future brings new flavors, line extensions, and very contemporary usage for Thornwell’s nostalgia brands.
These brands are all proudly produced in the USA, at the company’s headquarters in Canajoharie, New York.

We plan to participate in a candy specialty & gift trade show on September 10th.

Our booth size is 20' X 10'
Conceopt: Premium Candy Buffet

We need:

1. 4 banners (36" X 92" each) design (will create together the back wall):
- Keswick & Yardley Rock Candy sticks & Lantern Sticks
- Pelmarr candy sticks (covered with chocolate)
- Thornwell Gourmet Mints
- Chocolate covered fruits and nuts
2. Bring together all the elements (so we will know how to place them, and which color palate to use):
4 banners, 2 island tables (with candy jars on shelves and a Candy Bar) on top, a bar table with 2 chairs

Industry/Entity Type

Trade

Requirements
Must have
• - Logos (can be captured in each banner accordingly, or a banner that is dedicated to logos only
• - Images (current uploaded images are references only. High res images will be uploaded within few days
• - The images need to be over 150dpi and full bleed images (¼” bleed with no crop marks).

```html
<!DOCTYPE html>
<html lang="en">
<head>
<meta charset="utf-8">
<title>Chocolate Covered Fruit &amp; Nuts — Banner</title>
<link rel="stylesheet" href="https://fonts.googleapis.com/css2?family=Parisienne&family=Ultra&display=swap">
<style>
  :root {
    --banner-blue: #1b73b9;
    --accent-blue: #2aa4de;
    --ink: #0a0a0a;
    --white: #ffffff;
    --slate-dark: #5c6166;
    --slate-light: #8a8f94;
    --studio-white: #eef0f1;
    --studio-shade: #d9dcde;
  }
  * { margin: 0; padding: 0; box-sizing: border-box; }
  html, body {
    width: 1200px;
    height: 2866px;
    overflow: hidden;
    background: var(--banner-blue);
  }
  .banner {
    position: relative;
    width: 1200px;
    height: 2866px;
    background: var(--banner-blue);
    overflow: hidden;
  }
  .hero-photo {
    position: absolute;
    left: 0; top: 0;
    width: 1200px; height: 876px;
    background:
      radial-gradient(ellipse at 55% 40%, rgba(120,40,50,0.35) 0%, rgba(60,40,40,0.2) 35%, transparent 65%),
      linear-gradient(160deg, var(--slate-light) 0%, var(--slate-dark) 100%);
  }
  .headline-script {
    position: absolute;
    left: 0; top: 990px;
    width: 1200px;
    text-align: center;
    font-family: "Parisienne", cursive;
    font-size: 150px;
    line-height: 1;
    color: var(--white);
  }
  .headline-amp {
    position: absolute;
    left: 300px; top: 1290px;
    font-family: "Ultra", serif;
    font-size: 600px;
    line-height: 1;
    color: var(--accent-blue);
  }
  .headline-word {
    position: absolute;
    font-family: "Ultra", serif;
    font-size: 250px;
    line-height: 1;
    color: var(--ink);
  }
  .headline-word--fruit { left: 70px; top: 1250px; }
  .headline-word--nuts { left: 470px; top: 1700px; }
  .product-photo {
    position: absolute;
    left: 56px; top: 2150px;
    width: 1088px; height: 656px;
    background:
      radial-gradient(ellipse at 50% 65%, rgba(140,30,45,0.35) 0%, rgba(70,35,30,0.25) 35%, transparent 60%),
      linear-gradient(180deg, var(--studio-white) 0%, var(--studio-shade) 100%);
  }
</style>
</head>
<body>
  <main class="banner">
    <div class="hero-photo" role="img" aria-label="Photo of almonds, raspberries, blueberries and dark chocolate pieces scattered on a grey stone surface"></div>

    <h1 class="headline">
      <span class="headline-script">Chocolate Covered</span>
      <span class="headline-amp" aria-hidden="true">&amp;</span>
      <span class="headline-word headline-word--fruit">Fruit</span>
      <span class="headline-word headline-word--nuts">Nuts</span>
    </h1>

    <div class="product-photo" role="img" aria-label="Photo of chocolate covered candies with a strawberry, pomegranate, raspberry, blueberries and chocolate chunks on a white table"></div>
  </main>
</body>
</html>
```